Velto and Co Business Card Design

Looking for a business card design. Wanting Smart, Clean and Sharp looking to promote Velto and Co, our Import Export Business - like Black, White and natural textures. I have uploaded our logo. I like a rounded font but open to other ideas
Being that we have a wide range of products on offer we are looking for a neutral yet eye catching card. We would also like to have Import - Export on the business card to be clear on want our business does.

Target Market(s)

Import export market

Industry/Entity Type

Importer

Contact Information for Business Card

Mr Tobias Renwick
tobias.renwick@veltoandco.example.au
+61 (0) 412 731 846
www.veltoandco.example.au

Font styles to use
Other font styles liked:
• Unsure of actual font name but something rounded and clean

Colors

Designer to choose colors to be used in the design.

Requirements
Must have
• Instagram icon
• Facebook icon

```html
<!DOCTYPE html>
<html lang="en">
<head>
<meta charset="utf-8">
<title>Velto and Co Business Card</title>
<link href="https://fonts.googleapis.com/css2?family=PT+Sans:wght@400;700&family=Open+Sans:wght@400;600&display=swap" rel="stylesheet">
<style>
  :root {
    --bg: #d9d9d9;
    --paper: #f7f7f7;
    --ink: #231f20;
    --text: #1e1e1e;
    --white: #ffffff;
    --social-a: #3b5998;
    --social-b: #b07a5a;
  }
  * { margin: 0; padding: 0; box-sizing: border-box; }
  html, body { width: 1200px; height: 1200px; overflow: hidden; background: var(--bg); }
  .canvas { position: relative; width: 1200px; height: 1200px; }

  .card { position: absolute; left: 180px; width: 840px; height: 480px; overflow: hidden; }
  .card--front { top: 90px; background: var(--paper); }
  .card--back { top: 630px; background: var(--ink); }

  .name-plate {
    position: absolute; left: 58px; top: 89px; width: 388px; height: 91px;
    background: var(--ink); color: var(--white); padding: 12px 20px;
  }
  .name-plate__name { font: 700 34px/1.1 "PT Sans", sans-serif; letter-spacing: 0.2px; white-space: nowrap; }
  .name-plate__title { font: 400 20px/1.3 "Open Sans", sans-serif; margin-top: 4px; }

  .brand-block { position: absolute; display: flex; flex-direction: column; }
  .brand {
    display: flex; align-items: center; gap: 12px;
    font: 700 30px/1 "PT Sans", sans-serif; text-transform: uppercase; letter-spacing: 1px;
    white-space: nowrap;
  }
  .brand__square { width: 22px; height: 22px; background: currentColor; flex: none; }
  .brand-block__trade { font: 600 13px/1 "Open Sans", sans-serif; letter-spacing: 3px; text-transform: uppercase; margin-top: 12px; }

  .card--front .brand-block { right: 58px; top: 108px; align-items: flex-end; color: var(--ink); }
  .card--back .brand-block { left: 0; right: 0; top: 50%; transform: translateY(-50%); align-items: center; color: var(--white); }
  .card--back .brand { font-size: 56px; gap: 20px; }
  .card--back .brand__square { width: 40px; height: 40px; }
  .card--back .brand-block__trade { font-size: 18px; letter-spacing: 6px; margin-top: 20px; }

  .edge-tab { position: absolute; right: 0; top: 89px; width: 30px; height: 91px; background: var(--ink); }

  .rule { position: absolute; left: 58px; right: 58px; top: 328px; height: 2px; background: var(--ink); }

  .contact { position: absolute; left: 58px; top: 358px; list-style: none; }
  .contact li { display: flex; align-items: center; gap: 9px; font: 400 17px/27px "Open Sans", sans-serif; color: var(--text); white-space: nowrap; }
  .contact svg { width: 15px; height: 15px; flex: none; }

  .social { position: absolute; right: 58px; top: 410px; display: flex; align-items: center; gap: 8px; font: 400 17px/1 "Open Sans", sans-serif; color: var(--text); }
  .social__square { width: 15px; height: 15px; border-radius: 2px; }
  .social__square--a { background: var(--social-a); }
  .social__square--b { background: var(--social-b); }
</style>
</head>
<body>
<main class="canvas">
  <section class="card card--front" aria-label="Business card front">
    <div class="name-plate">
      <div class="name-plate__name">MR TOBIAS RENWICK</div>
      <div class="name-plate__title">CEO &amp; Manager</div>
    </div>
    <div class="brand-block">
      <div class="brand"><span class="brand__square"></span>Velto &amp; Co</div>
      <div class="brand-block__trade">Import - Export</div>
    </div>
    <div class="edge-tab"></div>
    <div class="rule"></div>
    <ul class="contact">
      <li>
        <svg viewBox="0 0 16 16" aria-hidden="true"><path d="M4 1.5l2.2 3-1.3 1.6c.9 2 2.5 3.6 4.5 4.5l1.6-1.3 3 2.2-1.2 2.5C7 13.5 2.5 9 1.5 2.7z" fill="#231f20"/></svg>
        call. +61 (0) 412 731 846
      </li>
      <li>
        <svg viewBox="0 0 16 16" aria-hidden="true"><rect x="2" y="3.5" width="12" height="9" rx="1" fill="none" stroke="#231f20" stroke-width="1.6"/><path d="M2.5 4.5L8 9l5.5-4.5" fill="none" stroke="#231f20" stroke-width="1.6"/></svg>
        tobias.renwick@veltoandco.example.au
      </li>
      <li>
        <svg viewBox="0 0 16 16" aria-hidden="true"><circle cx="8" cy="8" r="6.3" fill="none" stroke="#231f20" stroke-width="1.3"/><ellipse cx="8" cy="8" rx="2.8" ry="6.3" fill="none" stroke="#231f20" stroke-width="1.1"/><path d="M1.8 8h12.4M2.8 5h10.4M2.8 11h10.4" stroke="#231f20" stroke-width="1"/></svg>
        www.veltoandco.example.au
      </li>
    </ul>
    <div class="social">
      <span class="social__square social__square--a" role="img" aria-label="Social network profile"></span>
      <span class="social__square social__square--b" role="img" aria-label="Photo sharing profile"></span>
      /tobias.renwick
    </div>
  </section>

  <section class="card card--back" aria-label="Business card back">
    <div class="brand-block">
      <div class="brand"><span class="brand__square"></span>Velto &amp; Co</div>
      <div class="brand-block__trade">Import - Export</div>
    </div>
  </section>
</main>
</body>
</html>
```